File Download Website

We are looking for a design for a file download website. Our objective is to allow users to upload/browse/download files. This means we need 3 different pages.
The upload page should allow users to upload a file, we are looking for creative designs, a file box with a browse button next to it is already out there so the design must bring something new.
The browse page should display a users files/folders.
The download page should allow the user to download a file.
We do not require any code, only design. The designer is given complete freedom over the design, you may go about it however you like. This is a test of creativity, whoever this project goes to will definitely be given more work in the near future.
Example of a well designed file download website: cloudvessel.net
Target Market(s)
15-30 year old people
Industry/Entity Type
Work
Look and feel
Each slider illustrates characteristics of the customer's brand and the style your logo design should communicate.

```html
<!DOCTYPE html>
<html lang="en">
<head>
<meta charset="utf-8">
<title>File Download Website – Sign in</title>
<link href="https://fonts.googleapis.com/css2?family=Oswald:wght@400&family=Ubuntu:wght@400&family=Arimo:wght@400;700&display=swap" rel="stylesheet">
<style>
  :root {
    --header-bg: #deeefd;
    --header-line: #c3d6e8;
    --page-top: #ffffff;
    --page-mid: #e3effb;
    --page-low: #eef0f2;
    --footer-bg: #ebebeb;
    --footer-line: #d6d6d6;
    --ink: #111111;
    --mark: #9fb4c8;
    --step-green: #4aa22a;
    --step-green-dark: #3b8a1f;
    --link-blue: #19a3e0;
    --orange-top: #f09a32;
    --orange-bottom: #de7410;
    --field-border: #b9b9b9;
    --social-a: #3a6ea5;
    --social-b: #2fb4e6;
    --social-c: #1f9be0;
  }
  * { box-sizing: border-box; margin: 0; padding: 0; }
  html, body { width: 1200px; height: 886px; overflow: hidden; }
  body {
    position: relative;
    font-family: "Arimo", Arial, sans-serif;
    color: var(--ink);
    background: linear-gradient(180deg, var(--page-top) 146px, var(--page-mid) 300px, var(--page-low) 700px);
  }
  .site-header {
    position: absolute; left: 0; top: 0; width: 1200px; height: 146px;
    background: var(--header-bg);
    border-bottom: 1px solid var(--header-line);
  }
  .brand {
    position: absolute; display: flex; align-items: center; gap: 14px;
    font-family: "Arimo", Arial, sans-serif; font-weight: 700;
    color: var(--ink); white-space: nowrap;
  }
  .brand-mark { background: var(--mark); }
  .site-header .brand { left: 50%; top: 46px; transform: translateX(-50%); font-size: 36px; }
  .site-header .brand-mark { width: 52px; height: 52px; }
  .intro {
    position: absolute; left: 66px; top: 176px; width: 1068px;
    font-family: "Oswald", sans-serif; font-size: 19px; line-height: 32px;
    text-align: center; text-transform: uppercase; color: var(--ink);
  }
  .signin { position: absolute; left: 70px; top: 322px; width: 405px; }
  .signin-head { display: flex; justify-content: space-between; align-items: baseline; height: 36px; }
  .signin-title { font-size: 17px; font-weight: 700; }
  .signin-register { font-size: 14.5px; color: var(--ink); }
  .signin-register a { color: var(--link-blue); font-weight: 700; text-decoration: none; border-bottom: 1px dotted var(--link-blue); }
  .field {
    display: block; width: 405px; height: 44px; margin-bottom: 19px;
    border: 1px solid var(--field-border); border-radius: 3px; background: #fff;
    padding: 0 12px; line-height: 42px; font-size: 17px; color: var(--ink);
    box-shadow: inset 0 1px 2px rgba(0,0,0,.08);
  }
  .signin-actions { display: flex; justify-content: space-between; align-items: center; margin-top: -1px; }
  .btn-signin {
    width: 163px; height: 48px; border: 1px solid #c9670c; border-radius: 2px;
    background: linear-gradient(180deg, var(--orange-top), var(--orange-bottom));
    color: #fff; font-size: 16px; text-transform: uppercase; line-height: 46px; text-align: center;
  }
  .forgot { font-size: 14.5px; color: var(--link-blue); text-decoration: underline; }
  .divider { display: flex; align-items: center; gap: 22px; margin-top: 36px; color: #666; font-size: 17px; }
  .divider::before, .divider::after { content: ""; flex: 1; height: 1px; background: #d3d6da; }
  .social { display: flex; align-items: center; margin-top: 18px; }
  .social-label { font-size: 17px; font-weight: 700; width: 236px; }
  .social-btn { width: 45px; height: 45px; border-radius: 3px; margin-right: 12px; }
  .social-btn.a { background: var(--social-a); }
  .social-btn.b { background: var(--social-b); }
  .social-btn.c { background: var(--social-c); }
  .steps { position: absolute; left: 618px; top: 358px; display: flex; gap: 60px; }
  .step { width: 120px; text-align: center; font-family: "Ubuntu", sans-serif; font-size: 22px; line-height: 29px; }
  .step-icon { display: block; width: 96px; height: 96px; margin: 0 auto 12px; }
  .site-footer {
    position: absolute; left: 0; top: 701px; width: 1200px; height: 185px;
    background: var(--footer-bg); border-top: 1px solid var(--footer-line);
  }
  .site-footer .brand { left: 68px; top: 46px; font-size: 24px; gap: 10px; }
  .site-footer .brand-mark { width: 36px; height: 36px; }
  .footer-nav { position: absolute; top: 59px; left: 751px; display: flex; }
  .footer-nav a { font-size: 14px; color: var(--ink); text-decoration: underline; margin-right: 36px; }
</style>
</head>
<body>
  <header class="site-header">
    <div class="brand">File Download Website <span class="brand-mark"></span></div>
  </header>

  <p class="intro">Lorem ipsum dolor sit lorem ipsum dolor sit lorem ipsum dolor sit lorem ipsum dolor sitlorem ipsum dolor sit lorem ipsum dolor sit lorem ipsum dolor sit lorem ipsum dolor sit lorem ipsum dolor sit lorem ipsum dolor sit lorem ipsum dolor sit lorem ipsum dolor sitlorem ipsum dolor sit lorem ipsum dolor sit lorem ipsum dolor sit lorem ipsum dolor sit</p>

  <section class="signin">
    <div class="signin-head">
      <span class="signin-title">Sign in</span>
      <span class="signin-register">New to Fileharbor? <a href="#">Register</a></span>
    </div>
    <span class="field">Your e-mail</span>
    <span class="field">Your password</span>
    <div class="signin-actions">
      <span class="btn-signin">Sign me in</span>
      <a class="forgot" href="#">Forgot password?</a>
    </div>
    <div class="divider">Or</div>
    <div class="social">
      <span class="social-label">Sign in via social services</span>
      <span class="social-btn a" role="img" aria-label="Social network sign in"></span>
      <span class="social-btn b" role="img" aria-label="Social network sign in"></span>
      <span class="social-btn c" role="img" aria-label="Cloud storage sign in"></span>
    </div>
  </section>

  <section class="steps">
    <div class="step">
      <svg class="step-icon" viewBox="0 0 96 96" aria-hidden="true">
        <rect width="96" height="96" rx="3" fill="#4aa22a"/>
        <rect x="20" y="20" width="52" height="52" rx="9" fill="none" stroke="#fff" stroke-width="5"/>
        <path d="M46 44 L46 76 L54 68 L60 80 L66 77 L60 65 L71 65 Z" fill="#fff" stroke="#4aa22a" stroke-width="3"/>
      </svg>
      Upload<br>torrent
    </div>
    <div class="step">
      <svg class="step-icon" viewBox="0 0 96 96" aria-hidden="true">
        <rect width="96" height="96" rx="3" fill="#4aa22a"/>
        <path d="M38 18 H58 V46 H72 L48 74 L24 46 H38 Z" fill="#fff"/>
      </svg>
      Download<br>starts
    </div>
    <div class="step">
      <svg class="step-icon" viewBox="0 0 96 96" aria-hidden="true">
        <rect width="96" height="96" rx="3" fill="#4aa22a"/>
        <path d="M22 50 L31 41 L42 55 L70 24 L78 32 L42 72 Z" fill="#fff"/>
      </svg>
      You<br>got it!
    </div>
  </section>

  <footer class="site-footer">
    <div class="brand">File Download Website <span class="brand-mark"></span></div>
    <nav class="footer-nav">
      <a href="#">Privacy</a><a href="#">Terms</a><a href="#">Contact</a><a href="#">Sign in</a><a href="#">Register</a>
    </nav>
  </footer>
</body>
</html>
```